New Gay dating app for meeting new people

I am looking for someone to design me a new gay dating app. It should have features such as a sign in page, being able to upload pictures, make a profile, and be able to know the distance from someone and be able to send a location.

Could you please provide the finished product CODED and ready for use.

The colours are up to the designer.

The name of the app LumaVox

If you need to ask me any questions don't hesitate to ask me for anything.

Target Market(s)

Gay males 18+ years old

Industry/Entity Type

Dating

Requirements
Must have
• Be able to chat

```html
<!DOCTYPE html>
<html lang="en">
<head>
<meta charset="utf-8">
<title>LumaVox – Chat</title>
<link rel="stylesheet" href="https://fonts.googleapis.com/css2?family=Open+Sans:wght@300;400;600&display=swap">
<style>
  :root {
    --bg-deep: #232c37;
    --bg-mid: #2c3644;
    --bg-light: #354150;
    --bubble: #323d4b;
    --bubble-edge: #3e4a5a;
    --bar: #1e252f;
    --accent: #5fc3b4;
    --accent-soft: #4fa99c;
    --text: #e6ebef;
    --muted: #8a96a3;
    --badge: #e5484d;
    --star: #b9d36a;
    --avatar-a: #6d7a5a;
    --avatar-b: #5a4a40;
  }
  * { box-sizing: border-box; margin: 0; padding: 0; }
  html, body {
    width: 744px; height: 1200px; overflow: hidden;
    background: var(--bg-deep);
    font-family: "Open Sans", Arial, sans-serif;
    color: var(--text);
  }
  .screen {
    position: relative; width: 744px; height: 1200px; overflow: hidden;
    background:
      linear-gradient(118deg, transparent 0 46%, rgba(255,255,255,0.035) 46% 100%),
      linear-gradient(180deg, var(--bg-mid), var(--bg-deep));
  }
  .status-bar {
    height: 40px; display: flex; align-items: center; justify-content: space-between;
    padding: 0 22px; font-size: 17px; color: var(--muted);
  }
  .status-bar .time { position: absolute; left: 0; right: 0; text-align: center; pointer-events: none; }
  .nav-bar {
    height: 86px; display: flex; align-items: center; justify-content: space-between;
    padding: 0 30px; border-bottom: 1px solid rgba(255,255,255,0.04);
  }
  .app-title { font-size: 34px; font-weight: 300; color: var(--accent); letter-spacing: 0.5px; }
  .chat-list { position: relative; }
  .message { position: absolute; left: 0; width: 744px; height: 170px; }
  .avatar {
    position: absolute; top: 4px; width: 82px; height: 82px; border-radius: 50%;
    border: 3px solid #d8dde2;
  }
  .avatar.owen { left: 40px; background: radial-gradient(circle at 50% 40%, #8a9571, var(--avatar-a)); }
  .avatar.theo { right: 40px; background: radial-gradient(circle at 50% 40%, #7a6555, var(--avatar-b)); }
  .bubble {
    position: absolute; top: 0; width: 360px; padding: 14px 18px 16px;
    background: var(--bubble); border: 1px solid var(--bubble-edge); border-radius: 3px;
  }
  .message.incoming .bubble { left: 150px; }
  .message.outgoing .bubble { left: 224px; }
  .sender {
    font-size: 22px; font-weight: 400; color: var(--accent);
    padding-bottom: 8px; margin-bottom: 10px; border-bottom: 1px solid var(--bubble-edge);
  }
  .text { font-size: 15px; line-height: 1.45; color: var(--text); }
  .stamp {
    position: absolute; top: 18px; display: flex; align-items: center; gap: 8px;
    font-size: 15px; color: var(--muted);
  }
  .message.incoming .stamp { left: 560px; }
  .message.outgoing .stamp { left: 120px; }
  .tab-bar {
    position: absolute; left: 0; right: 0; bottom: 0; height: 108px;
    background: var(--bar); display: flex; align-items: center; justify-content: space-around;
  }
  .tab { position: relative; width: 60px; height: 60px; display: flex; align-items: center; justify-content: center; }
  .badge {
    position: absolute; top: 8px; right: 8px; width: 14px; height: 14px; border-radius: 50%;
    background: var(--badge);
  }
</style>
</head>
<body>
<main class="screen">
  <header class="status-bar">
    <span>●●●●○ NOVA</span>
    <span class="time">4:21 PM</span>
    <span>100%</span>
  </header>

  <nav class="nav-bar">
    <svg width="22" height="36" viewBox="0 0 22 36" aria-label="Back"><path d="M18 4 L5 18 L18 32" fill="none" stroke="var(--muted)" stroke-width="3"/></svg>
    <h1 class="app-title">LumaVox</h1>
    <svg width="34" height="26" viewBox="0 0 34 26" aria-label="Menu"><g stroke="var(--muted)" stroke-width="3"><line x1="0" y1="3" x2="34" y2="3"/><line x1="0" y1="13" x2="34" y2="13"/><line x1="0" y1="23" x2="34" y2="23"/></g></svg>
  </nav>

  <section class="chat-list">
    <article class="message incoming" style="top:52px">
      <div class="avatar owen" role="img" aria-label="Profile photo of Owen Marsh"></div>
      <div class="bubble">
        <p class="sender">Owen Marsh</p>
        <p class="text">Hi there! I would like to go out tonight at Rivet, care to join me &amp; friends? :)</p>
      </div>
      <span class="stamp"><svg width="16" height="16" viewBox="0 0 16 16"><circle cx="8" cy="8" r="6.5" fill="none" stroke="var(--muted)" stroke-width="1.5"/><path d="M8 4 V8 H11" fill="none" stroke="var(--muted)" stroke-width="1.5"/></svg>21:40</span>
    </article>

    <article class="message outgoing" style="top:246px">
      <span class="stamp"><svg width="16" height="16" viewBox="0 0 16 16"><circle cx="8" cy="8" r="6.5" fill="none" stroke="var(--muted)" stroke-width="1.5"/><path d="M8 4 V8 H11" fill="none" stroke="var(--muted)" stroke-width="1.5"/></svg>21:44</span>
      <div class="bubble">
        <p class="sender">Theo Barnes</p>
        <p class="text">That sounds great! :) I am available for tonight it would be a great party!<br>Should I pick you up?<br>Clara and Dean are coming too.</p>
      </div>
      <div class="avatar theo" role="img" aria-label="Profile photo of Theo Barnes"></div>
    </article>

    <article class="message incoming" style="top:462px">
      <div class="avatar owen" role="img" aria-label="Profile photo of Owen Marsh"></div>
      <div class="bubble">
        <p class="sender">Owen Marsh</p>
        <p class="text">Hi there! I would like to go out tonight at Rivet, care to join me &amp; friends? :)</p>
      </div>
      <span class="stamp"><svg width="16" height="16" viewBox="0 0 16 16"><circle cx="8" cy="8" r="6.5" fill="none" stroke="var(--muted)" stroke-width="1.5"/><path d="M8 4 V8 H11" fill="none" stroke="var(--muted)" stroke-width="1.5"/></svg>21:46</span>
    </article>

    <article class="message outgoing" style="top:656px">
      <span class="stamp"><svg width="16" height="16" viewBox="0 0 16 16"><circle cx="8" cy="8" r="6.5" fill="none" stroke="var(--muted)" stroke-width="1.5"/><path d="M8 4 V8 H11" fill="none" stroke="var(--muted)" stroke-width="1.5"/></svg>21:44</span>
      <div class="bubble">
        <p class="sender">Theo Barnes</p>
        <p class="text">That sounds great! :) I am available for tonight it would be a great party!<br>Should I pick you up?<br>Clara and Dean are coming too.</p>
      </div>
      <div class="avatar theo" role="img" aria-label="Profile photo of Theo Barnes"></div>
    </article>
  </section>

  <footer class="tab-bar">
    <div class="tab" aria-label="Profile">
      <svg width="40" height="40" viewBox="0 0 40 40"><g fill="none" stroke="var(--accent-soft)" stroke-width="2"><circle cx="20" cy="14" r="8"/><path d="M5 37 C7 27 13 24 20 24 C27 24 33 27 35 37 Z"/></g></svg>
    </div>
    <div class="tab" aria-label="Chats">
      <svg width="42" height="40" viewBox="0 0 42 40"><g fill="none" stroke="var(--accent-soft)" stroke-width="2"><path d="M21 5 C31 5 38 11 38 19 C38 27 31 33 21 33 C18 33 16 32.5 14 32 L6 36 L8.5 29 C5.5 26 4 23 4 19 C4 11 11 5 21 5 Z"/></g><g fill="var(--accent-soft)"><circle cx="14" cy="19" r="2"/><circle cx="21" cy="19" r="2"/><circle cx="28" cy="19" r="2"/></g></svg>
      <span class="badge"></span>
    </div>
    <div class="tab" aria-label="Favourites">
      <svg width="40" height="40" viewBox="0 0 40 40"><path d="M20 3 L25 15 L38 15.5 L28 24 L31.5 37 L20 29.5 L8.5 37 L12 24 L2 15.5 L15 15 Z" fill="none" stroke="var(--star)" stroke-width="2" stroke-linejoin="round"/></svg>
    </div>
  </footer>
</main>
</body>
</html>
```